Luxury Business Card Design for High-End Window Treatments

Gilded Vantages
Custom Plantation Shutters & Architectural Shading Systems

⸻

BACK

Daniel Forsythe
Owner

Custom Interior & Exterior Window Treatments

919-482-7034
gildedvantages.com

I have included a picture that I’m hoping we can use on the back, but I’m also wondering if you can get rid of the ladder? Should we get rid of shutters , shades and blinds underneath Gilded Vantages?

Target Market(s)

High-end residential homeowners, custom home builders, architects, interior designers, and luxury renovation clients seeking premium plantation shutters and motorized architectural shading systems.

Industry/Entity Type

Custom Window treatments

Contact Information for Business Card

Front Gilded Vantages Custom Plantation Shutters Motorized Architectural Shading Systems BACK Daniel Forsythe Owner 919-482-7034 GildedVantages.com Custom Interior & Exterior Window Treatments By Appointment

Requirements
Nice to have
• Not 100% sure on nice to halves or the color but you can definitely check out my website to get a better understanding of what I’m trying to do

```html
<!DOCTYPE html>
<html lang="en">
<head>
<meta charset="utf-8">
<title>Gilded Vantages — Business Card</title>
<link rel="stylesheet" href="https://fonts.googleapis.com/css2?family=Cormorant+Garamond:ital,wght@0,500;0,600;1,500&display=swap">
<style>
  :root {
    --backdrop: #1b1d24;
    --card: #232326;
    --card-deep: #17171a;
    --gold: #c9a55a;
    --ivory: #ecebe6;
    --muted: #b9b8b3;
    --rule: #6a6a6c;
    --photo-sky: #5a6270;
    --photo-house: #3a3d44;
    --photo-glow: #8a7a58;
    --photo-ground: #2a2d2a;
  }
  * { box-sizing: border-box; margin: 0; padding: 0; }
  html, body { width: 1200px; height: 775px; overflow: hidden; }
  body {
    background: var(--backdrop);
    font-family: "Cormorant Garamond", Georgia, serif;
    color: var(--ivory);
    display: flex;
    align-items: center;
    justify-content: center;
    gap: 36px;
  }
  .card {
    width: 560px;
    height: 320px;
    border-radius: 16px;
    background: linear-gradient(160deg, var(--card) 0%, var(--card-deep) 100%);
    position: relative;
    overflow: hidden;
  }

  /* Front */
  .card-front {
    display: flex;
    flex-direction: column;
    align-items: center;
    justify-content: center;
    text-align: center;
  }
  .brand-name {
    font-weight: 500;
    font-size: 64px;
    line-height: 0.98;
    color: var(--gold);
    margin-bottom: 34px;
  }
  .services {
    font-weight: 500;
    font-size: 22px;
    line-height: 1.35;
    color: var(--ivory);
    letter-spacing: 0.3px;
  }

  /* Back */
  .card-back .scene-photo {
    position: absolute;
    left: 0; top: 0;
    width: 62%;
    height: 100%;
    background:
      linear-gradient(90deg, transparent 55%, var(--card-deep) 100%),
      linear-gradient(180deg, var(--photo-sky) 0%, var(--photo-house) 35%, var(--photo-glow) 60%, var(--photo-ground) 100%);
  }
  .contact-block {
    position: absolute;
    left: 322px;
    top: 30px;
    right: 22px;
  }
  .person-name {
    font-weight: 600;
    font-size: 28px;
    line-height: 1.1;
  }
  .person-role {
    font-style: italic;
    font-size: 19px;
    color: var(--muted);
    margin-bottom: 22px;
  }
  .tagline {
    font-weight: 500;
    font-size: 19px;
    line-height: 1.25;
    padding-bottom: 14px;
    border-bottom: 1px solid var(--rule);
    margin-bottom: 14px;
    max-width: 220px;
  }
  .contact-line {
    display: flex;
    align-items: center;
    gap: 10px;
    font-weight: 500;
    font-size: 20px;
    margin-bottom: 8px;
  }
  .contact-line svg { width: 17px; height: 17px; flex: none; }
  .availability {
    font-style: italic;
    font-size: 18px;
    color: var(--muted);
    margin-top: 14px;
  }
</style>
</head>
<body>
  <section class="card card-front">
    <h1 class="brand-name">Gilded<br>Vantages</h1>
    <p class="services">Custom Plantation Shutters<br>Motorized Architectural Shading Systems</p>
  </section>

  <section class="card card-back">
    <div class="scene-photo" role="img" aria-label="Evening photograph of a columned home porch with screened windows, lit interior and lawn chairs"></div>
    <div class="contact-block">
      <h2 class="person-name">Daniel Forsythe</h2>
      <p class="person-role">Owner</p>
      <p class="tagline">Custom Interior &amp; Exterior Window Treatments</p>
      <p class="contact-line">
        <svg viewBox="0 0 24 24" aria-hidden="true"><path fill="#ecebe6" d="M6.6 10.8a15.1 15.1 0 0 0 6.6 6.6l2.2-2.2c.3-.3.7-.4 1-.2 1.1.4 2.3.6 3.6.6.6 0 1 .4 1 1V20c0 .6-.4 1-1 1A17 17 0 0 1 3 4c0-.6.4-1 1-1h3.5c.6 0 1 .4 1 1 0 1.3.2 2.5.6 3.6.1.3 0 .7-.2 1z"/></svg>
        919-482-7034
      </p>
      <p class="contact-line">
        <svg viewBox="0 0 24 24" aria-hidden="true" fill="none" stroke="#ecebe6" stroke-width="1.8"><circle cx="12" cy="12" r="9"/><ellipse cx="12" cy="12" rx="4" ry="9"/><line x1="3" y1="12" x2="21" y2="12"/></svg>
        gildedvantages.com
      </p>
      <p class="availability">By Appointment</p>
    </div>
  </section>
</body>
</html>
```